Werbebanner für Textilreinigung
Zielgruppe
Wir sind eine Textilreinigung mit einem großen Spektrum an Leistungen.
Unsere Zielgruppe sind Privat Personen die ihre Textilien zum reinigen zu uns bringen.
Aufgabenstellung
Es sollen 5 Straßenbanner designt werden. Diese werden bei Ortseinfahrten/- ausfahrten, aufgehängt. Das Design soll modern sein und zu unserem Logo passen. Die Herausforderung bei den Straßenbannern ist die Zielgruppe, die Autofahrer. Der Banner wird beim Vorbeifahren für nur 1-2 Sekunden gesehen. Auf jedem Banner soll ein Sonderangebot mit eingebaut werden. Zu der Zeit in der der Banner aufgehängt ist, erhält der Kunde 20% auf die jeweilige Dienstleistung.
Hier die verschiedenen Banner:
-Betten & Daunenreinigung | -Trachten und Lederreinigung | -Braut & Festtagskleider reinigung |-Teppichwäsche (inkl. kostenlosen Abhol und Lieferservice) |-Hemdenservice
Bannergröße beträgt 100cm(H) x 300cm(B)
Das gilt für alle 5 verschiedenen Banner.
Es soll auf jedem Banner stehen:
-Sonderangebot 20%
-unser Logo (siehe Dateien)
-unsere Adresse
-Telefonnummer
-Aufruf zur Aktion
Anmerkung: Auf der EPS.Datei muss ein kleiner Schriftzug hinzugefügt werden der auf der PDF. zu sehen ist.

```html
<!DOCTYPE html>
<html lang="de">
<head>
<meta charset="utf-8">
<title>Banner Trachten und Lederreinigung</title>
<link rel="stylesheet" href="https://fonts.googleapis.com/css2?family=Roboto+Condensed:wght@400;700;800&display=swap">
<style>
  :root {
    --page-bg: #d4d4d4;
    --banner-bg: #ffffff;
    --brand-red: #b3121b;
    --brand-blue: #2b3a94;
    --brand-green: #6cb52d;
    --photo-light: #e9e6e3;
    --photo-mid: #c9c3bf;
    --white: #ffffff;
  }
  * { margin: 0; padding: 0; box-sizing: border-box; }
  html, body { width: 1200px; height: 1200px; overflow: hidden; }
  body {
    background: var(--page-bg);
    font-family: "Roboto Condensed", "Arial Narrow", sans-serif;
    position: relative;
  }
  .banner {
    position: absolute;
    left: 30px; top: 410px;
    width: 1140px; height: 380px;
    background: var(--banner-bg);
    overflow: hidden;
  }
  .banner-shapes { position: absolute; inset: 0; }
  .service-title {
    position: absolute;
    left: 375px; top: 36px;
    width: 765px; height: 80px;
    background: var(--brand-red);
    color: var(--white);
    font-weight: 700;
    font-size: 56px;
    line-height: 80px;
    padding-left: 24px;
    letter-spacing: 0.2px;
  }
  .offer {
    position: absolute;
    left: 520px; top: 130px;
    width: 170px;
    color: var(--brand-red);
    text-align: center;
    font-weight: 800;
    transform: rotate(-4deg);
  }
  .offer-call { display: block; font-size: 28px; line-height: 30px; }
  .offer-value { display: block; font-size: 86px; line-height: 80px; letter-spacing: -2px; }
  .offer-verb { display: block; font-size: 44px; line-height: 46px; }
  .brand {
    position: absolute;
    left: 735px; top: 188px;
    display: flex; align-items: center; gap: 18px;
  }
  .brand-dot {
    width: 64px; height: 64px; border-radius: 50%;
    background: var(--brand-green);
    flex: none;
  }
  .brand-text { color: var(--brand-blue); }
  .brand-tagline { font-size: 19px; line-height: 21px; font-weight: 400; }
  .brand-name { font-size: 58px; line-height: 56px; font-weight: 700; }
  .contact-line {
    position: absolute;
    left: 350px; top: 303px;
    width: 790px; height: 77px;
    color: var(--white);
    display: flex; align-items: center; justify-content: center; gap: 12px;
    font-weight: 700;
    white-space: nowrap;
  }
  .contact-town { font-size: 30px; }
  .contact-street { font-size: 40px; }
  .contact-phone { font-size: 30px; display: flex; align-items: center; gap: 8px; }
  .contact-sep { font-size: 30px; }
</style>
</head>
<body>
  <section class="banner">
    <svg class="banner-shapes" viewBox="0 0 1140 380" width="1140" height="380">
      <defs>
        <linearGradient id="photoTone" x1="0" y1="0" x2="1" y2="1">
          <stop offset="0" stop-color="var(--photo-light)"/>
          <stop offset="1" stop-color="var(--photo-mid)"/>
        </linearGradient>
      </defs>
      <path class="photo-area" role="img" aria-label="Foto: lächelndes Paar in bayerischer Tracht, Frau im Dirndl, Mann mit Hut und Lederhose"
            d="M0 0 H545 C470 110 420 230 330 380 H0 Z" fill="url(#photoTone)"/>
      <path class="contact-band" d="M330 303 H1140 V380 H285 Z" fill="var(--brand-blue)"/>
      <path class="accent-curve" d="M548 -4 C470 120 430 230 310 300 C290 315 270 345 255 384"
            fill="none" stroke="var(--brand-green)" stroke-width="9" stroke-linecap="round"/>
    </svg>

    <h1 class="service-title">Trachten und Lederreinigung</h1>

    <p class="offer">
      <span class="offer-call">JETZT</span>
      <span class="offer-value">20%</span>
      <span class="offer-verb">SPAREN!</span>
    </p>

    <div class="brand">
      <span class="brand-dot"></span>
      <div class="brand-text">
        <p class="brand-tagline">ZENTRALREINIGUNG<br>GROSSWÄSCHEREI</p>
        <p class="brand-name">GLANZWERK</p>
      </div>
    </div>

    <p class="contact-line">
      <span class="contact-town">ALTENRIED</span>
      <span class="contact-sep">•</span>
      <span class="contact-street">LINDENSTRASSE 8</span>
      <span class="contact-sep">•</span>
      <span class="contact-phone">
        <svg width="24" height="24" viewBox="0 0 24 24" aria-hidden="true">
          <path d="M6.6 10.8a15.1 15.1 0 0 0 6.6 6.6l2.2-2.2a1 1 0 0 1 1-.25 11.4 11.4 0 0 0 3.6.57 1 1 0 0 1 1 1V20a1 1 0 0 1-1 1A17 17 0 0 1 3 4a1 1 0 0 1 1-1h3.5a1 1 0 0 1 1 1c0 1.25.2 2.45.57 3.57a1 1 0 0 1-.25 1z" fill="var(--white)"/>
        </svg>
        01234 - 5678
      </span>
    </p>
  </section>
</body>
</html>
```